Scientific project description

Here is a project description related to cellular mechanics, showing above the forces acting on cells in the tissues of our body. The forces on single cells are there to depict how forces are acting on cells (pressure squeezes the cell, shear flow is pushing the upward parts of the cell, tension pulls one part of the cell, strain is stretching the whole cell; the single cell images are to be found also on the last page). Intense red/purple are used to indicate that the forces are stressful (the colors to be used do not need to be exactly like these colors). The picture in the middle is a view of cells (same picture on next page if that needs to be modified). At the left, a description of what happens when everything is going well, i.e. the body stays healthy. At the right, if you dysfunction you get disease. Green nuances were used to indicate health, brownish, perhaps not so pleasant nuances were used to indicate disease. Below are the steps of the project.

On the whole, we're rather happy with the concept description as such, but it should look a little bit nicer. To many color nuances give a "noisy" impression, fonts could be nicer, layout more crisp, and the text on the steps should be more readable. We would also like to have two versions of the same picture, one with black background, one with white.

Target Market(s)

Scientists that are evaluating our project

Requirements
Must have
• Easy to grasp the idea, easy to read and understand the underlying idea.
Nice to have
• Would be good to have the Concept title ("Vorlint Concept and Envisioned Project Progression) on top of the figure as indicated in the second brief picture submitted.

```html
<!DOCTYPE html>
<html lang="en">
<head>
<meta charset="utf-8">
<title>Vorlint Concept and Envisioned Project Progression</title>
<link href="https://fonts.googleapis.com/css2?family=Open+Sans:ital,wght@0,400;0,600;0,700;1,700&display=swap" rel="stylesheet">
<style>
  :root {
    --bg: #000;
    --text: #fff;
    --pressure: #ff0a0a;
    --shear: #950a3c;
    --tension: #a50000;
    --strain: #c414dc;
    --band-top: #000;
    --band-bottom: #8a8a8a;
    --node: #1e1e1e;
    --step: #1c1c1c;
    --health: #7cf032;
    --fitness-edge: #3a9a1e;
    --disease: #c8500f;
    --frailty-edge: #c8500f;
  }
  * { margin: 0; padding: 0; box-sizing: border-box; }
  html, body { width: 1200px; height: 850px; overflow: hidden; background: var(--bg); }
  body { font-family: "Open Sans", sans-serif; color: var(--text); position: relative; }

  .title {
    position: absolute; top: 40px; left: 0; width: 1200px; text-align: center;
    font-size: 38px; font-weight: 700; font-style: italic; letter-spacing: 0.2px;
  }
  .force-band {
    position: absolute; left: 131px; top: 122px; width: 941px; height: 180px;
    background: linear-gradient(to bottom, var(--band-top), var(--band-bottom));
  }
  .band-label {
    position: absolute; right: 26px; bottom: 6px; font-size: 16px; font-weight: 700;
    font-style: italic; color: #111;
  }
  .force {
    position: absolute; top: 18px; width: 212px; height: 112px; border-radius: 50%;
    text-align: center; font-size: 20px; padding-top: 6px;
  }
  .force-pressure { left: 17px; background: var(--pressure); }
  .force-shear { left: 247px; background: var(--shear); }
  .force-tension { left: 479px; background: var(--tension); }
  .force-strain { left: 709px; background: var(--strain); }
  .force-icon {
    display: block; width: 130px; height: 56px; margin: 8px auto 0; border-radius: 50%;
    background: rgba(255,255,255,0.18);
  }

  .links { position: absolute; left: 0; top: 0; }

  .cell-view {
    position: absolute; left: 476px; top: 312px; width: 248px; height: 248px; border-radius: 50%;
    background: radial-gradient(circle, #2f6a1e 0%, #1c4a12 55%, #0a1d06 85%, #000 100%);
  }
  .cell-view-label {
    position: absolute; left: 476px; top: 418px; width: 248px; text-align: center;
    font-size: 24px; font-weight: 700; font-style: italic;
  }

  .tag {
    position: absolute; font-size: 15px; padding: 2px 8px; border-radius: 14px; border: 1.5px solid;
  }
  .tag-fitness { left: 243px; top: 337px; border-color: var(--fitness-edge); }
  .tag-frailty { left: 871px; top: 336px; border-color: var(--frailty-edge); }

  .node {
    position: absolute; top: 382px; width: 148px; height: 100px; border-radius: 50%;
    background: var(--node); font-size: 15px; line-height: 19px; text-align: center;
    display: flex; align-items: center; justify-content: center;
  }
  .node-functional { left: 215px; }
  .node-dysfunctional { left: 844px; }

  .outcome { position: absolute; top: 572px; width: 240px; text-align: center; font-size: 30px; font-weight: 700; }
  .outcome-health { left: 169px; color: var(--health); }
  .outcome-disease { left: 797px; color: var(--disease); }

  .steps { position: absolute; left: 0; top: 0; width: 1200px; }
  .step {
    position: absolute; background: var(--step); text-align: center;
    font-size: 21px; line-height: 30px; height: 30px;
  }
</style>
</head>
<body>
  <h1 class="title">Vorlint Concept&nbsp; and Envisioned Project Progression</h1>

  <div class="force-band">
    <div class="force force-pressure">Pressure<span class="force-icon" role="img" aria-label="Cell being squeezed by pressure from above"></span></div>
    <div class="force force-shear">Shear<span class="force-icon" role="img" aria-label="Cell pushed sideways by shear flow"></span></div>
    <div class="force force-tension">Tension<span class="force-icon" role="img" aria-label="Cell pulled upward at one point by tension"></span></div>
    <div class="force force-strain">Strain<span class="force-icon" role="img" aria-label="Cell stretched at both ends by strain"></span></div>
    <div class="band-label">Forces on cells</div>
  </div>

  <svg class="links" width="1200" height="850" viewBox="0 0 1200 850" aria-hidden="true">
    <defs>
      <marker id="head-pressure" markerWidth="4" markerHeight="4" refX="2" refY="2" orient="auto"><path d="M0,0 L4,2 L0,4z" fill="#e00000"/></marker>
      <marker id="head-shear" markerWidth="4" markerHeight="4" refX="2" refY="2" orient="auto"><path d="M0,0 L4,2 L0,4z" fill="#80082f"/></marker>
      <marker id="head-tension" markerWidth="4" markerHeight="4" refX="2" refY="2" orient="auto"><path d="M0,0 L4,2 L0,4z" fill="#9a0000"/></marker>
      <marker id="head-strain" markerWidth="4" markerHeight="4" refX="2" refY="2" orient="auto"><path d="M0,0 L4,2 L0,4z" fill="#b010c8"/></marker>
      <marker id="head-white" markerWidth="6" markerHeight="6" refX="3" refY="3" orient="auto"><path d="M0,0 L6,3 L0,6z" fill="#fff"/></marker>
    </defs>
    <line x1="304" y1="244" x2="402" y2="332" stroke="#e00000" stroke-width="12" marker-end="url(#head-pressure)"/>
    <line x1="488" y1="252" x2="524" y2="306" stroke="#80082f" stroke-width="12" marker-end="url(#head-shear)"/>
    <line x1="712" y1="252" x2="676" y2="306" stroke="#9a0000" stroke-width="12" marker-end="url(#head-tension)"/>
    <line x1="896" y1="244" x2="800" y2="334" stroke="#b010c8" stroke-width="12" marker-end="url(#head-strain)"/>
    <line x1="462" y1="434" x2="410" y2="434" stroke="#fff" stroke-width="2" marker-end="url(#head-white)"/>
    <line x1="738" y1="434" x2="790" y2="434" stroke="#fff" stroke-width="2" marker-end="url(#head-white)"/>
    <line x1="289" y1="512" x2="289" y2="552" stroke="#fff" stroke-width="2" marker-end="url(#head-white)"/>
    <line x1="917" y1="512" x2="917" y2="552" stroke="#fff" stroke-width="2" marker-end="url(#head-white)"/>
  </svg>

  <div class="cell-view" role="img" aria-label="Fluorescence microscopy view of cells in green with red highlights"></div>
  <div class="cell-view-label">Mechanostasis</div>

  <div class="tag tag-fitness">Cell Fitness</div>
  <div class="tag tag-frailty">Cell Frailty</div>

  <div class="node node-functional">Functional<br>Cellular<br>Machineries</div>
  <div class="node node-dysfunctional">Dysfunctional<br>Cellular<br>Machineries</div>

  <div class="outcome outcome-health">HEALTH</div>
  <div class="outcome outcome-disease">DISEASE</div>

  <div class="steps">
    <div class="step" style="left:513px;top:579px;width:197px;">Therapies</div>
    <div class="step" style="left:491px;top:611px;width:240px;">Prevention</div>
    <div class="step" style="left:482px;top:642px;width:256px;">Critical Targets</div>
    <div class="step" style="left:471px;top:673px;width:280px;">Cellular Machineries</div>
    <div class="step" style="left:461px;top:709px;width:300px;">Disease Models</div>
    <div class="step" style="left:446px;top:745px;width:330px;">Cell, tissue &amp; organ response</div>
    <div class="step" style="left:426px;top:782px;width:370px;">Mechanical Force models</div>
  </div>
</body>
</html>
```